Social Media Graphics - Harbor Climb REVISED

Create 6-7 individual social media graphics (square size) to encourage folks to join our online course called:

The Lantern Ledger Plan
How to Launch a Multi-Million Business From Scratch
Sign Up Today!

IMPORTANT: Make the largest and most prominent text on the graphic be: How to Launch a Multi-Million Business From Scratch

For the color scheme of the graphics, let's try a blue color palette; make sure the graphics appeal to both men and women

Make sure each graphic contains 1 of the 3 pics attached (crop pic as needed); and make sure one of the graphics is all TEXT only.

Target Market(s)

men and women looking to start a business

Industry/Entity Type

Entrepreneurship

Colors
0054AA
0677BA
7BADD7
CADEEF
E8F1F8

Requirements
Must have
• All the text and use the 3 pics provided; one graphic can be all text; Simple, modern design that's easy to read

```html
<!DOCTYPE html>
<html lang="en">
<head>
<meta charset="utf-8">
<title>The Lantern Ledger Plan – Social Graphic</title>
<link rel="stylesheet" href="https://fonts.googleapis.com/css2?family=Anton&family=Montserrat:wght@400;500;600;800;900&display=swap">
<style>
  :root {
    --stage: #66a3c6;
    --navy-deep: #041a5e;
    --navy: #0a2a86;
    --royal: #0054aa;
    --bright: #0677ba;
    --sky: #1ea2f0;
    --pink: #ef3a63;
    --white: #ffffff;
    --button-navy: #0b1f6e;
  }
  * { margin: 0; padding: 0; box-sizing: border-box; }
  html, body {
    width: 1200px; height: 862px; overflow: hidden;
    background: var(--stage);
  }
  .post {
    position: absolute; left: 190px; top: 21px;
    width: 820px; height: 820px; overflow: hidden;
    background:
      radial-gradient(circle at 95% 5%, var(--sky) 0%, rgba(30,162,240,0) 45%),
      linear-gradient(160deg, var(--navy) 0%, var(--royal) 55%, var(--navy-deep) 100%);
    font-family: "Montserrat", sans-serif;
    color: var(--white);
  }
  .post > svg.arc { position: absolute; inset: 0; }
  .photo {
    position: absolute; left: 380px; top: 165px; width: 440px; height: 655px;
    background: linear-gradient(180deg, rgba(30,40,80,0.55) 0%, #161a2a 45%, #10131f 100%);
    border-top-left-radius: 180px;
  }
  .headline { position: absolute; left: 30px; white-space: nowrap; line-height: 1; text-shadow: 0 3px 8px rgba(0,0,20,0.35); }
  .headline--title { top: 52px; font-weight: 800; font-size: 90px; letter-spacing: -1px; }
  .headline--sub { top: 168px; font-family: "Anton", sans-serif; font-size: 74px; letter-spacing: 0.5px; }
  .tag { position: absolute; line-height: 1; white-space: nowrap; display: flex; align-items: center; justify-content: center; }
  .tag--howto {
    left: 40px; top: 302px; width: 236px; height: 62px;
    background: var(--white); color: var(--royal);
    font-weight: 500; font-size: 50px; transform: rotate(-3deg);
  }
  .tag--launch {
    left: 82px; top: 362px; width: 318px; height: 50px;
    background: var(--pink); color: var(--white);
    font-weight: 500; font-size: 46px;
  }
  .hero { position: absolute; left: 38px; white-space: nowrap; line-height: 1; text-shadow: 0 3px 8px rgba(0,0,20,0.4); }
  .hero--multi { top: 428px; font-family: "Anton", sans-serif; font-size: 104px; }
  .hero--business { top: 548px; font-weight: 900; font-size: 82px; }
  .hero--from { top: 630px; font-weight: 400; font-size: 62px; }
  .hero--scratch { top: 695px; font-weight: 800; font-size: 70px; }
  .cta {
    position: absolute; left: 516px; top: 702px; width: 266px; height: 58px;
    border: 4px solid var(--white); border-radius: 30px;
    background: var(--button-navy);
    display: flex; align-items: center; justify-content: center;
    font-weight: 800; font-size: 24px; letter-spacing: 0.3px;
    box-shadow: 0 4px 10px rgba(0,0,0,0.35);
  }
</style>
</head>
<body>
  <main class="post">
    <svg class="arc" width="820" height="820" viewBox="0 0 820 820" aria-hidden="true">
      <circle cx="640" cy="840" r="400" fill="none" stroke="var(--pink)" stroke-width="44"/>
    </svg>
    <div class="photo" role="img" aria-label="Photo of the two smiling course hosts, a man in a black turtleneck with arms crossed and a woman in a blue jacket"></div>

    <h1 class="headline headline--title">THE LANTERN</h1>
    <p class="headline headline--sub">LEDGER PLAN</p>

    <span class="tag tag--howto">HOW TO</span>
    <span class="tag tag--launch">LAUNCH A</span>

    <h2 class="hero hero--multi">MULTI-MILLION</h2>
    <p class="hero hero--business">BUSINESS</p>
    <p class="hero hero--from">FROM</p>
    <p class="hero hero--scratch">SCRATCH</p>

    <div class="cta">SIGN UP TODAY!</div>
  </main>
</body>
</html>
```